Real Estate Agent need a business card

I am a real estate agent in Vancouver, BC Canada. I recently used PixelHarbor to develop a logo of my own. I would like to have my logo in the business card, as well my realty office logo also must be displayed along with its address. I also would like to have my headshot photo displayed in the business card on both sides.

Industry/Entity Type

Real Estate Agent

Contact Information for Business Card

My office address:
Bramwell Peak Realty
2271 Lindqvist St.
Vancouver, BC V5K 2P8

My contact information:
Cell: 604-555-0148
Office: 604-555-0192
Fax: 604-555-0193

My website : www.danielmorvik.example
My email: email@danielmorvik.example

My slogan: Simply I do. Far and Above.

Requirements
Must have
• Front side(all in colour): My photo, My own logo, My office logo, My cell number, My website address and email, My slogan.
• Back side(could be black & white/ plz refer to the file name "preview"): My photo, My own logo, my office logo, my office address, my contact information.
• * Please read this: Since my logo has my name in it, there is no need to put my name in the card separately. As well, my office logo MUST BE displayed on both sides(you can reduce the size of office logo). But the office address can be displayed only one side, front or back. I would prefer to have my cell number only to be displayed prominently on the front side. So all the numbers should be displayed on the backside instead. Remember that I am trying to promote myself so the most important thing I consider from the front side of the card is my cell number, my website, and my email, not the office. The only thing I require by industry regulation from the front side is my office logo. Hope this helps.
Nice to have
• Colour on the front side and the black and white on the back side

```html
<!DOCTYPE html>
<html lang="en">
<head>
<meta charset="utf-8">
<title>Daniel Morvik – Business Card Concepts</title>
<link rel="stylesheet" href="https://fonts.googleapis.com/css2?family=Source+Sans+3:wght@400;600;700&display=swap">
<style>
  :root {
    --board: #1f1f1f;
    --paper: #ffffff;
    --ink: #111111;
    --ink-soft: #3a3d40;
    --lime: #8cff0f;
    --mint: #4cfa8c;
    --sun: #fff200;
    --brand-green: #8cd21e;
    --bar: #111111;
    --photo-light: #d9dde2;
    --photo-dark: #2d3644;
    --photo-gray-light: #e6e6e6;
    --photo-gray-dark: #6e6e6e;
  }
  * { box-sizing: border-box; margin: 0; padding: 0; }
  html, body { width: 1200px; height: 498px; overflow: hidden; background: var(--board); }
  body { font-family: "Source Sans 3", "Myriad Pro", sans-serif; position: relative; }

  .card {
    position: absolute;
    width: 378px;
    height: 216px;
    background: var(--paper);
    overflow: hidden;
  }
  .card--front-lime  { left: 16px;  top: 22px; --accent: var(--lime); }
  .card--front-mint  { left: 410px; top: 22px; --accent: var(--mint); }
  .card--front-sun   { left: 806px; top: 22px; --accent: var(--sun); --front-text: var(--ink); --bubble-bg: var(--ink); --bubble-text: var(--paper); }
  .card--back-centre { left: 12px;  top: 256px; }
  .card--back-left   { left: 410px; top: 256px; }

  /* agent wordmark */
  .agent-mark {
    position: absolute;
    display: flex;
    align-items: center;
    gap: 4px;
    font-weight: 700;
    color: var(--ink-soft);
    white-space: nowrap;
  }
  .agent-mark__square { width: 10px; height: 10px; background: var(--brand-green); flex: none; }

  /* office wordmark */
  .office-mark {
    position: absolute;
    font-weight: 700;
    color: var(--ink);
    text-align: center;
    line-height: 1.05;
  }

  .headshot { position: absolute; }

  /* front */
  .front__photo-panel { position: absolute; left: 0; top: 0; width: 152px; height: 216px; background: var(--paper); }
  .front__photo-panel .agent-mark { left: 20px; top: 14px; font-size: 11px; }
  .front__photo-panel .headshot {
    left: 0; top: 40px; width: 152px; height: 176px;
    background: radial-gradient(ellipse at 55% 35%, #e4c4aa 0 18%, transparent 19%),
                linear-gradient(180deg, var(--photo-light) 0%, var(--photo-light) 55%, var(--photo-dark) 56%, var(--photo-dark) 100%);
  }
  .front__color-panel { position: absolute; left: 152px; top: 0; width: 226px; height: 216px; background: var(--accent); color: var(--front-text, var(--paper)); }
  .front__color-panel .office-mark { right: 12px; top: 18px; width: 96px; font-size: 11px; }

  .slogan-bubble { position: absolute; left: 10px; top: 40px; width: 68px; height: 50px; }
  .slogan-bubble svg { position: absolute; inset: 0; }
  .slogan-bubble__text {
    position: absolute; inset: 0; display: flex; flex-direction: column;
    align-items: center; justify-content: center; padding-bottom: 6px;
    font-size: 7.5px; line-height: 1.75; color: var(--bubble-text, var(--accent));
  }

  .front__details { position: absolute; left: 14px; top: 143px; }
  .front__name { font-size: 11.5px; font-weight: 700; letter-spacing: 0.1px; line-height: 1.2; }
  .front__title { font-size: 6.5px; font-weight: 700; margin-bottom: 9px; }
  .front__contact { font-size: 6.5px; font-weight: 600; line-height: 1.6; }

  /* back */
  .card--back-centre .office-mark { left: 22px; top: 18px; width: 110px; font-size: 12px; }
  .card--back-centre .agent-mark { right: 22px; top: 46px; font-size: 12px; }
  .card--back-centre .headshot { left: 96px; top: 0; width: 184px; height: 216px; }
  .card--back-left .headshot { left: 0; top: 0; width: 180px; height: 216px; }
  .card--back-left .office-mark { left: 240px; top: 22px; width: 120px; font-size: 12px; }
  .card--back-left .agent-mark { left: 240px; top: 132px; font-size: 12px; }
  .headshot--mono {
    background: radial-gradient(ellipse at 50% 32%, #cfcfcf 0 16%, transparent 17%),
                linear-gradient(180deg, var(--photo-gray-light) 0%, var(--photo-gray-light) 58%, var(--photo-gray-dark) 59%, var(--photo-gray-dark) 100%);
  }

  .contact-bar {
    position: absolute; top: 176px; height: 34px;
    background: var(--bar); color: var(--paper);
    font-size: 8px; line-height: 1.5;
    display: flex; flex-direction: column; justify-content: center;
    padding: 0 8px;
  }
  .card--back-centre .contact-bar { left: 46px; width: 286px; align-items: center; }
  .card--back-left .contact-bar { left: 0; width: 286px; }
  .contact-bar strong { font-weight: 700; }
</style>
</head>
<body>

  <!-- Front: lime -->
  <section class="card card--front-lime">
    <div class="front__photo-panel">
      <div class="agent-mark"><span class="agent-mark__square"></span>DANIEL MORVIK</div>
      <div class="headshot" role="img" aria-label="Headshot of the agent in a dark suit"></div>
    </div>
    <div class="front__color-panel">
      <div class="slogan-bubble">
        <svg viewBox="0 0 68 50" aria-hidden="true"><ellipse cx="35" cy="23" rx="33" ry="22" fill="var(--bubble-bg, #fff)"/><path d="M6 34 L2 46 L16 40 Z" fill="var(--bubble-bg, #fff)"/></svg>
        <div class="slogan-bubble__text"><span>Simply I do</span><span>Far and Above</span></div>
      </div>
      <div class="office-mark">Bramwell Peak Realty</div>
      <div class="front__details">
        <p class="front__name">DANIEL MORVIK</p>
        <p class="front__title">Real Estate Agent</p>
        <p class="front__contact">Tel: 604-555-0148<br>Web: www.danielmorvik.example<br>Email: email@danielmorvik.example</p>
      </div>
    </div>
  </section>

  <!-- Front: mint -->
  <section class="card card--front-mint">
    <div class="front__photo-panel">
      <div class="agent-mark"><span class="agent-mark__square"></span>DANIEL MORVIK</div>
      <div class="headshot" role="img" aria-label="Headshot of the agent in a dark suit"></div>
    </div>
    <div class="front__color-panel">
      <div class="slogan-bubble">
        <svg viewBox="0 0 68 50" aria-hidden="true"><ellipse cx="35" cy="23" rx="33" ry="22" fill="var(--bubble-bg, #fff)"/><path d="M6 34 L2 46 L16 40 Z" fill="var(--bubble-bg, #fff)"/></svg>
        <div class="slogan-bubble__text"><span>Simply I do</span><span>Far and Above</span></div>
      </div>
      <div class="office-mark">Bramwell Peak Realty</div>
      <div class="front__details">
        <p class="front__name">DANIEL MORVIK</p>
        <p class="front__title">Real Estate Agent</p>
        <p class="front__contact">Tel: 604-555-0148<br>Web: www.danielmorvik.example<br>Email: email@danielmorvik.example</p>
      </div>
    </div>
  </section>

  <!-- Front: yellow -->
  <section class="card card--front-sun">
    <div class="front__photo-panel">
      <div class="agent-mark"><span class="agent-mark__square"></span>DANIEL MORVIK</div>
      <div class="headshot" role="img" aria-label="Headshot of the agent in a dark suit"></div>
    </div>
    <div class="front__color-panel">
      <div class="slogan-bubble">
        <svg viewBox="0 0 68 50" aria-hidden="true"><ellipse cx="35" cy="23" rx="33" ry="22" fill="var(--bubble-bg, #fff)"/><path d="M6 34 L2 46 L16 40 Z" fill="var(--bubble-bg, #fff)"/></svg>
        <div class="slogan-bubble__text"><span>Simply I do</span><span>Far and Above</span></div>
      </div>
      <div class="office-mark">Bramwell Peak Realty</div>
      <div class="front__details">
        <p class="front__name">DANIEL MORVIK</p>
        <p class="front__title">Real Estate Agent</p>
        <p class="front__contact">Tel: 604-555-0148<br>Web: www.danielmorvik.example<br>Email: email@danielmorvik.example</p>
      </div>
    </div>
  </section>

  <!-- Back: centred portrait -->
  <section class="card card--back-centre">
    <div class="headshot headshot--mono" role="img" aria-label="Black and white headshot of the agent"></div>
    <div class="office-mark">Bramwell Peak Realty</div>
    <div class="agent-mark"><span class="agent-mark__square"></span>DANIEL MORVIK</div>
    <div class="contact-bar">
      <p><strong>Office address:</strong> 2271 Lindqvist St. Vancouver, BC V5K 2P8</p>
      <p><strong>My contact:</strong> Tel: 604-555-0148 | Office: 604-555-0192 | Fax: 604-555-0193</p>
    </div>
  </section>

  <!-- Back: left portrait -->
  <section class="card card--back-left">
    <div class="headshot headshot--mono" role="img" aria-label="Black and white headshot of the agent"></div>
    <div class="office-mark">Bramwell Peak Realty</div>
    <div class="agent-mark"><span class="agent-mark__square"></span>DANIEL MORVIK</div>
    <div class="contact-bar">
      <p><strong>Office address:</strong> 2271 Lindqvist St. Vancouver, BC V5K 2P8</p>
      <p><strong>My contact:</strong> Tel: 604-555-0148 | Office: 604-555-0192 | Fax: 604-555-0193</p>
    </div>
  </section>

</body>
</html>
```